Splash Screen for a new release of software

Our company Tarnwell Asia Pacific writes business management software for the automotive industry. Early next year we are planning on releasing our new version of Velquira, this is a fourth generation product. Our thoughts are to brand this version simply Velquira 4, however we do wish to add a certain exclusivity to product hence the addition of Premier Edition as a signature to the Velquira brand. The splash screen has to make the user feel that they are using an upmarket product and are excited to be doing so. I have uploaded an "in house" design for reference purposes, also included our sphere company logo.

```html
<!DOCTYPE html>
<html lang="en">
<head>
<meta charset="UTF-8">
<title>Velquira 4 – Premier Edition Splash Screen</title>
<link rel="stylesheet" href="https://fonts.googleapis.com/css2?family=Montserrat:wght@900&family=Outfit:wght@300;400;600&family=Orbitron:wght@400&display=swap">
<style>
  :root {
    --page-bg: #ffffff;
    --night: #141040;
    --deep-blue: #15257a;
    --royal-blue: #2348c4;
    --violet: #3a2c96;
    --sky-cyan: #2cb8f4;
    --white: #ffffff;
    --badge: #8a1257;
  }
  * { margin: 0; padding: 0; box-sizing: border-box; }
  html, body {
    width: 1200px; height: 1000px; overflow: hidden;
    background: var(--page-bg);
  }
  .splash {
    position: absolute;
    left: 12px; top: 60px;
    width: 1176px; height: 880px;
    border-radius: 52px;
    overflow: hidden;
    background: var(--deep-blue);
  }
  .stage-scene {
    position: absolute; inset: 0;
    background:
      radial-gradient(ellipse 50% 55% at 55% 55%, rgba(60, 130, 240, 0.55), transparent 70%),
      linear-gradient(100deg, var(--night) 0%, var(--deep-blue) 30%, var(--royal-blue) 62%, var(--violet) 100%);
  }
  .edition {
    position: absolute; left: 56px; top: 96px;
    font-family: 'Outfit', sans-serif; font-weight: 300;
    font-size: 70px; line-height: 1.1; color: var(--sky-cyan);
  }
  .product-name {
    position: absolute; left: 0; top: 270px; width: 1176px; text-align: center;
    font-family: 'Montserrat', sans-serif; font-weight: 900;
    font-size: 164px; line-height: 1; letter-spacing: 6px;
    color: var(--white);
    text-shadow: 0 0 18px rgba(80, 160, 255, 0.9), 0 0 50px rgba(60, 130, 255, 0.7);
  }
  .version {
    position: absolute; right: 52px; top: 430px;
    font-family: 'Orbitron', sans-serif; font-weight: 400;
    font-size: 50px; line-height: 1; letter-spacing: 18px; color: var(--white);
    transform: skewX(-12deg);
    text-shadow: 0 0 10px rgba(80, 160, 255, 0.8);
  }
  .brand {
    position: absolute; left: 932px; top: 565px; width: 200px; height: 200px;
    border-radius: 50%;
    background: var(--badge);
    display: flex; align-items: center; justify-content: center;
  }
  .brand-name {
    font-family: 'Outfit', sans-serif; font-weight: 600;
    font-size: 24px; letter-spacing: 2px; color: var(--white);
  }
  .release-date, .copyright {
    position: absolute; top: 818px;
    font-family: 'Outfit', sans-serif; font-weight: 400;
    font-size: 20px; letter-spacing: 2.4px; color: var(--white);
  }
  .release-date { left: 62px; }
  .copyright { right: 64px; }
</style>
</head>
<body>
  <main class="splash">
    <div class="stage-scene" role="img" aria-label="Illuminated blue stage with a glowing giant numeral 4, light beams, grid floor and a round display podium"></div>

    <p class="edition">Premier Edition</p>
    <h1 class="product-name">VELQUIRA</h1>
    <p class="version">VERSION 4.0.0</p>

    <div class="brand">
      <span class="brand-name">TARNWELL</span>
    </div>

    <p class="release-date">January, 21.2025</p>
    <p class="copyright">Tarnwell Asia Pacific Pty Ltd 2016</p>
  </main>
</body>
</html>
```